Tall-Anchor Brochure

We would like a 3 panel layout format with copy on both sides and on each panel, (we will provide content).

We are Tall-Anchor and we work with business owners to achieve measurable growth and success based on 6 Core Pillars Of Momentum and (S.B.L) 90 Day Steady Build Ledger. We also work with the business leader and individuals within the organization with personal development.

We would like the brochure to have a corporate feel, but warm and inviting. We don't want a hard or aggressive feel.

We would like it to be available for pdf upload and physical print formats.

The winning design will also be invited to design a header for our website as well. The header will be consistent with the brochure, so please keep that in mind during your creative process.

I am enclosing a transparent copy of our company logo along with content for the brochure.

Thank you in advance for your consideration!

Gordon and Moira
Updates

Sorry, but we forgot to include the front cover text.

It will read as follows,

Do you know the 6 Core Pillars Of Momentum  that are crucial to the success of any business today?

Also, please add the following to the back page

Website: www.tall-anchor.example
Resource Centre: www.taresources.example 
Phone: +44 (0) 7812056417
Email: info@tall-anchor.example

Follow us on (please insert Facelog, Workline and Clipstream logo)

I have uploaded a pdf format of brochure text.

Hello designers. I wanted to give some further input to help the process. Although the brochure is to target business, we don't want to over do it with corporate professioanls in all the photos. If there is an opportunity to incorporate photos of small business owners like, a butcher, baker, chef, flower shop etc. This would hopefully help us make an immpression to all small business owners.

Thank you, and good luck!

Gordon and Moira  

Reason: A few designers have come come on board last minute. So I'd like to give everyone the same opportunity to respond. Sincerely, Gordon

Target Market(s)

Small Business Owners searching for new ways to grow their business in the UK and Republic Of Ireland.

Industry/Entity Type

Business

```html
<!DOCTYPE html>
<html lang="en">
<head>
<meta charset="utf-8">
<title>Tall-Anchor Brochure – Outside</title>
<link rel="stylesheet" href="https://fonts.googleapis.com/css2?family=Open+Sans:wght@400;600;700&family=Anton&display=swap">
<style>
  :root{
    --page:#ffffff;
    --ink:#5b2357;
    --grey:#555;
    --purple:#6e2a6e;
    --purple-dark:#551d57;
    --purple-mid:#8a3b8c;
    --pink-accent:#f07ce8;
    --art-pink:#edc6ee;
    --art-lilac:#dcd0ec;
  }
  *{margin:0;padding:0;box-sizing:border-box}
  html,body{width:1200px;height:857px;overflow:hidden;background:var(--page)}
  body{position:relative;font-family:"Open Sans",Arial,sans-serif;color:var(--ink)}
  .sheet-label{position:absolute;left:1018px;top:30px;font-size:32px;color:var(--grey);font-weight:400}
  .brochure{position:absolute;left:93px;top:97px;width:1018px;height:720px;background:#fff;box-shadow:0 0 6px rgba(0,0,0,.25);overflow:hidden}
  .panel{position:absolute;top:0;height:720px;width:339px;overflow:hidden}
  .panel--left{left:0;background:linear-gradient(180deg,#fbf4fb,#fff 40%,#fbf2fb)}
  .panel--middle{left:339px;background:#fff}
  .panel--cover{left:677px;width:341px;background:#fff}
  .bg-bands{position:absolute;inset:0}
  .ribbon{position:absolute;color:#fff;font-size:15px;display:flex;align-items:center;justify-content:center}
  .ribbon svg{position:absolute;inset:0;overflow:visible}
  .ribbon span{position:relative}
  .copy{position:absolute;font-size:13.6px;line-height:19.5px;color:var(--ink);text-align:justify}
  .copy p{text-indent:56px}
  .copy strong{color:#5a4a58;font-weight:700}
  .areas{position:absolute;left:32px;top:387px;list-style:none;font-size:13.6px;line-height:19.5px}
  .areas li{position:relative;padding-left:30px}
  .areas li::before{content:"";position:absolute;left:4px;top:6px;width:6px;height:6px;border-right:2px solid #666;border-top:2px solid #666;transform:rotate(45deg)}
  .photo-slot{position:absolute;left:0;top:0;width:339px;height:215px;clip-path:polygon(0 0,100% 0,100% 47%,0 100%);background:linear-gradient(135deg,#5a5a5e 0%,#b79c92 50%,#b9a3c2 100%)}
  .wordmark{position:absolute;display:flex;align-items:center;gap:8px;font-family:"Open Sans",Arial,sans-serif;font-weight:600;letter-spacing:2.5px;color:var(--purple)}
  .wordmark i{display:block;background:var(--purple)}
  .contact{position:absolute;left:62px;top:390px;list-style:none;font-size:14.5px;color:#333}
  .contact li{display:flex;align-items:center;height:41px}
  .contact .icon{width:31px;height:31px;margin-right:22px;flex:none}
  .resource{position:absolute;left:0;width:339px;top:524px;text-align:center;font-size:14.5px;line-height:22px;color:#333}
  .social{position:absolute;left:124px;top:596px;list-style:none;font-size:13.6px;color:#222}
  .social li{display:flex;align-items:center;height:23px}
  .social .dot{width:11px;height:11px;background:var(--purple-mid);margin-right:17px}
  .cover-headline{position:absolute;left:22px;top:222px;width:306px;font-family:"Anton",Impact,sans-serif;font-weight:400;font-size:23.5px;line-height:30px;color:#fff;text-align:center;transform:rotate(-12deg);letter-spacing:.3px}
  .cover-headline em{font-style:normal;color:var(--pink-accent)}
  .growth-art{position:absolute;left:15px;top:372px;width:318px;height:262px;background:linear-gradient(160deg,var(--art-pink),var(--art-lilac))}
</style>
</head>
<body>
  <div class="sheet-label">Outside</div>

  <main class="brochure">
    <section class="panel panel--left">
      <svg class="bg-bands" width="339" height="720" aria-hidden="true">
        <polygon points="0,70 339,0 339,30 0,100" fill="#f2dff2"/>
        <polygon points="0,85 339,20 339,40 0,105" fill="#f8eaf8"/>
        <polygon points="0,650 339,590 339,625 0,690" fill="#f4e3f4"/>
        <polygon points="0,690 339,630 339,720 0,720" fill="#faf1fa"/>
      </svg>

      <div class="ribbon" style="left:64px;top:36px;width:211px;height:54px">
        <svg width="211" height="54" aria-hidden="true">
          <polygon points="195,0 211,14 211,54 195,40" fill="var(--purple-dark)"/>
          <polygon points="0,14 211,14 211,54 0,54" fill="var(--purple)"/>
          <polygon points="0,54 14,54 14,64" fill="var(--purple-dark)"/>
        </svg>
        <span style="top:7px">Getting Started!</span>
      </div>

      <div class="copy" style="left:25px;top:126px;width:290px">
        <p>The first step is to visit <strong>www.tall-anchor.example</strong> or call <strong>07812056417</strong> to book your <strong>FREE CONSULTATION</strong>. This will be an opportunity for you to think about where you want your business to go and for us to establish how we can get you there.</p>
      </div>

      <div class="ribbon" style="left:0;top:272px;width:156px;height:38px">
        <svg width="156" height="38" aria-hidden="true">
          <polygon points="140,0 156,9 156,38 140,30" fill="var(--purple-dark)"/>
          <polygon points="0,9 156,9 156,38 0,38" fill="var(--purple)"/>
        </svg>
        <span style="top:4px;left:-14px;font-size:14px">After That?</span>
      </div>

      <div class="copy" style="left:25px;top:329px;width:290px">
        <p>We will carry out a business analysis based on <strong>The 6 Core Pillars of Momentum.</strong></p>
      </div>

      <ul class="areas">
        <li>Your Brand</li>
        <li>Sales</li>
        <li>Your People</li>
        <li>Product &amp; Service</li>
        <li>Psychology &amp; Skills</li>
        <li>Finance</li>
      </ul>

      <div class="copy" style="left:25px;top:526px;width:290px">
        <p>We then provide you with a detailed report and work with you to create and implement your Steady Build Ledger (S.B.L). This is a 90 day plan, customized for your business and designed so you can start seeing positive and measurable results immediately.</p>
      </div>
    </section>

    <section class="panel panel--middle">
      <svg class="bg-bands" width="339" height="720" aria-hidden="true">
        <polygon points="0,480 339,420 339,445 0,505" fill="#f6e8f6"/>
        <polygon points="0,500 339,440 339,455 0,515" fill="#fbf3fb"/>
      </svg>
      <div class="photo-slot" role="img" aria-label="Photo of a hand lifting a desk telephone receiver"></div>

      <div class="ribbon" style="left:65px;top:218px;width:211px;height:52px">
        <svg width="211" height="52" aria-hidden="true">
          <polygon points="196,0 211,14 211,52 196,38" fill="var(--purple-dark)"/>
          <polygon points="0,14 211,14 211,52 0,52" fill="var(--purple)"/>
          <polygon points="0,52 18,52 18,68" fill="var(--purple-dark)"/>
        </svg>
        <span style="top:7px">Get in Touch!</span>
      </div>

      <div class="wordmark" style="left:86px;top:320px;font-size:17px">
        <i style="width:14px;height:14px"></i>TALL-ANCHOR
      </div>

      <ul class="contact">
        <li>
          <svg class="icon" viewBox="0 0 31 31" aria-hidden="true"><polygon points="0,5 31,0 31,26 0,31" fill="var(--purple)"/><text x="15.5" y="21" fill="#fff" font-size="13" font-weight="700" text-anchor="middle" font-family="Open Sans,sans-serif">W</text></svg>
          www.tall-anchor.example
        </li>
        <li>
          <svg class="icon" viewBox="0 0 31 31" aria-hidden="true"><polygon points="0,5 31,0 31,26 0,31" fill="var(--purple)"/><path d="M10 20c3 3 6 3 8 1l-2-2-1 1c-1 0-3-2-3-3l1-1-2-2c-2 2-2 4-1 6z" fill="#fff"/></svg>
          +44 (0) 7812056417
        </li>
        <li>
          <svg class="icon" viewBox="0 0 31 31" aria-hidden="true"><polygon points="0,5 31,0 31,26 0,31" fill="var(--purple)"/><text x="15.5" y="21" fill="#fff" font-size="14" font-weight="700" text-anchor="middle" font-family="Open Sans,sans-serif">@</text></svg>
          info@tall-anchor.example
        </li>
      </ul>

      <p class="resource">Visit our Resource Center at<br>www.taresource.example</p>

      <ul class="social">
        <li><span class="dot"></span>Facelog!</li>
        <li><span class="dot"></span>Workline!</li>
        <li><span class="dot"></span>Clipstream!</li>
      </ul>
    </section>

    <section class="panel panel--cover">
      <svg class="bg-bands" width="341" height="720" aria-hidden="true">
        <polygon points="0,0 110,0 0,35" fill="#ecd3ec"/>
        <polygon points="0,170 341,105 341,135 0,200" fill="#f1dcf1"/>
        <polygon points="0,205 341,130 341,155 0,230" fill="#f8ecf8"/>
        <polygon points="0,238 341,165 341,345 0,412" fill="var(--purple)"/>
        <polygon points="0,238 341,165 341,200 0,270" fill="var(--purple-mid)" opacity=".6"/>
        <polygon points="5,412 63,400 63,428" fill="var(--purple-dark)"/>
        <polygon points="0,420 341,370 341,395 0,445" fill="#e9cbe9"/>
        <polygon points="0,660 341,585 341,720 0,720" fill="var(--purple)"/>
      </svg>

      <div class="wordmark" style="left:80px;top:64px;font-size:17px">
        <i style="width:14px;height:14px"></i>TALL-ANCHOR
      </div>

      <h1 class="cover-headline">Do you know the <em>6 Core Pillars Of Momentum</em> that are crucial to the success of any business today?</h1>

      <div class="growth-art" role="img" aria-label="Illustration of a rising growth arrow above the word profit"></div>
    </section>
  </main>
</body>
</html>
```